electrical company- Company name- Voltmark Trades, slogan- All installations and servicingcolours to stick roughly with logo- greys, blues, black, white. simple yet effective- logo to stand out and attention to name also (gareth). Modern design.

Industry/Entity Type

Business

Contact Information for Business Card

gareth WilliamsElectrician021 994 306info@voltmarktrades.co.nzwww.voltmarktrades.co.nzPO box 5367Palmerston North, 4472

```html
<!DOCTYPE html>
<html lang="en">
<head>
<meta charset="utf-8">
<title>Voltmark Trades – Business Card</title>
<link rel="stylesheet" href="https://fonts.googleapis.com/css2?family=Lato:wght@400;700;900&display=swap">
<style>
  :root {
    --page: #f4f4f4;
    --card-blue: #1487c8;
    --bright-blue: #1d9fdc;
    --ink: #0b0b0b;
    --paper: #ffffff;
    --steel: #808080;
  }
  html, body {
    margin: 0;
    width: 1200px;
    height: 960px;
    overflow: hidden;
    background: var(--page);
  }
  .stage {
    position: relative;
    width: 1200px;
    height: 960px;
  }
  .card {
    position: absolute;
    top: 165px;
    width: 373px;
    height: 630px;
    border-radius: 10px;
    overflow: hidden;
  }
  .card--front { left: 200px; }
  .card--back { left: 637px; }
  .card svg { display: block; }
  .card text { font-family: "Lato", sans-serif; }
  .fill-blue { fill: var(--card-blue); }
  .fill-bright { fill: var(--bright-blue); }
  .fill-ink { fill: var(--ink); }
  .fill-paper { fill: var(--paper); }
  .fill-steel { fill: var(--steel); }
  .outline { fill: none; stroke: var(--paper); stroke-width: 1.5; }
  .holder-name { font-weight: 900; font-size: 19px; fill: var(--bright-blue); }
  .holder-role { font-weight: 400; font-size: 15px; fill: var(--paper); }
  .address { font-weight: 400; font-size: 17px; fill: var(--paper); }
  .phone { font-weight: 400; font-size: 19px; fill: var(--ink); }
  .contact { font-weight: 400; font-size: 14.5px; fill: var(--ink); }
  .social { font-weight: 400; font-size: 15px; fill: var(--paper); }
  .brand-name { font-weight: 900; letter-spacing: 1px; text-transform: uppercase; }
  .brand-name--front { font-size: 25px; fill: var(--paper); }
  .brand-name--top { font-size: 30px; fill: var(--paper); }
  .brand-name--band { font-size: 26px; fill: var(--card-blue); }
</style>
</head>
<body>
<main class="stage">

  <!-- Front: holder details -->
  <section class="card card--front">
    <svg width="373" height="630" viewBox="0 0 373 630">
      <rect class="fill-blue" width="373" height="630"/>
      <polygon class="fill-ink" points="0,108 373,-138 373,-54 0,192"/>
      <polygon class="fill-paper" points="0,192 373,-54 373,-49 0,197"/>
      <polygon class="fill-ink" points="0,197 373,-49 373,-26 0,220"/>
      <polygon class="fill-paper" points="0,220 373,-26 373,139 0,385"/>
      <polygon class="fill-bright" points="30,200 373,-26 373,37 30,263"/>
      <polygon class="fill-ink" points="0,385 373,139 373,209 0,455"/>

      <text class="holder-name" transform="translate(32 122) rotate(-33.4)">Gareth Pemberly</text>
      <text class="holder-role" transform="translate(45 138) rotate(-33.4)">Electrician</text>

      <text class="address" transform="translate(52 202) rotate(-33.4)">PO Box 8142</text>
      <text class="address" transform="translate(62 226) rotate(-33.4)">Palmerston North 4472, NZ</text>

      <g class="icon-phone" transform="translate(38 300) rotate(-33.4) scale(0.8)">
        <path class="fill-bright" d="M-7,-9 h5 l1,4 -2,2 a9,9 0 0 0 5,5 l2,-2 4,1 v5 a2,2 0 0 1 -2,2 a14,14 0 0 1 -14,-14 a2,2 0 0 1 1,-3z"/>
      </g>
      <g class="icon-mail" transform="translate(50 318) rotate(-33.4)">
        <rect class="fill-bright" x="-6" y="-8" width="12" height="8" rx="1"/>
        <path d="M-6,-8 L0,-3 L6,-8" fill="none" stroke="#ffffff" stroke-width="1.2"/>
      </g>
      <g class="icon-screen" transform="translate(61 334) rotate(-33.4)">
        <rect x="-6" y="-10" width="12" height="8" rx="1" fill="none" stroke="var(--bright-blue)" stroke-width="1.6"/>
        <rect class="fill-bright" x="-3" y="-1" width="6" height="2"/>
      </g>

      <text class="phone" transform="translate(55 303) rotate(-33.4)">021 573 814</text>
      <text class="contact" transform="translate(64 316) rotate(-33.4)">info@voltmarktrades-example.co.nz</text>
      <text class="contact" transform="translate(75 330) rotate(-33.4)">www.voltmarktrades-example.co.nz</text>

      <rect class="fill-bright" width="10" height="10" transform="translate(87 355) rotate(-33.4) translate(0 -10)"/>
      <rect class="fill-bright" width="10" height="10" transform="translate(97 372) rotate(-33.4) translate(0 -10)"/>
      <text class="social" transform="translate(105 355) rotate(-33.4)">voltmarktrades.nz/news</text>
      <text class="social" transform="translate(115 372) rotate(-33.4)">voltmarktrades.nz/reviews</text>

      <rect class="fill-steel" x="146" y="460" width="80" height="80"/>
      <text class="brand-name brand-name--front" x="186.5" y="595" text-anchor="middle">Voltmark Trades</text>
    </svg>
  </section>

  <!-- Back: brand face -->
  <section class="card card--back">
    <svg width="373" height="630" viewBox="0 0 373 630">
      <rect class="fill-blue" width="373" height="630"/>

      <rect class="fill-steel" x="133" y="70" width="110" height="110"/>
      <text class="brand-name brand-name--top" x="188" y="232" text-anchor="middle">Voltmark Trades</text>

      <!-- outlined panels -->
      <polyline class="outline" points="0,250 185,392 108,435 0,355"/>
      <polygon class="outline" points="203,357 373,242 373,262 218,368"/>

      <!-- left wedge -->
      <polygon class="fill-ink" points="0,355 108,435 0,516"/>

      <!-- parallel lower bands, slope 0.75 -->
      <polygon class="fill-ink" points="58,553.5 341,341.25 341,359.25 58,571.5"/>
      <polygon class="fill-ink" points="0,628 373,348.25 373,372.25 0,652"/>
      <polygon class="fill-paper" points="0,675 373,395.25 373,480.25 0,760"/>
      <polygon class="fill-ink" points="0,780 373,500.25 373,630 0,630"/>

      <text class="brand-name brand-name--band" transform="translate(150 615) rotate(-36.87)">Voltmark Trades</text>
    </svg>
  </section>

</main>
</body>
</html>
```